RW Frameworks Inc Business cards

We need business cards using our existing logo but slightly modified. Right now the logo says RW Framework Masonry. We want to keep the RW part of the design, but replace the Framework Masonry portion with "FRAMEWORKS". Please see the attached file.
Ideally this would be a blank template so we can add Different Names, titles, and phone numbers later.
On the one side we want only the logo and on the other side the detail. I'm attaching an example for you to see.
Please reach out with any other questions. Our address and other details will be given out once we find a design we like.

Target Market(s)

Construction Industry

```html
<!DOCTYPE html>
<html lang="en">
<head>
<meta charset="UTF-8">
<title>RW Frameworks Inc Business Cards</title>
<link rel="stylesheet" href="https://fonts.googleapis.com/css2?family=Montserrat:wght@400;500;600;700&display=swap">
<style>
  :root {
    --backdrop: #2a7fe9;
    --card-white: #ffffff;
    --card-dark: #1f1f1f;
    --brand-blue: #1c73bd;
    --ink: #1a1a1a;
  }
  * { box-sizing: border-box; margin: 0; padding: 0; }
  html, body {
    width: 1200px; height: 900px; overflow: hidden;
    background: var(--backdrop);
    font-family: "Montserrat", sans-serif;
  }
  .stage {
    width: 1200px; height: 900px;
    display: flex; align-items: center; justify-content: center; gap: 40px;
  }
  .card {
    position: relative;
    width: 540px; height: 309px;
    box-shadow: 0 18px 40px rgba(10, 40, 110, 0.35);
  }
  .card--details { background: var(--card-white); color: var(--ink); }
  .card--logo {
    background: var(--card-dark);
    display: flex; flex-direction: column; align-items: center; justify-content: center;
  }
  .accent-bar {
    position: absolute; top: 66px; left: 300px;
    width: 176px; height: 18px; background: var(--brand-blue);
  }
  .person { position: absolute; left: 40px; top: 40px; }
  .person__name { font-weight: 700; font-size: 24px; letter-spacing: 0.3px; }
  .person__title { font-size: 11px; color: var(--brand-blue); margin-top: 2px; }
  .person__dash {
    width: 22px; height: 3px; background: var(--brand-blue); margin-top: 18px;
  }
  .company { position: absolute; left: 40px; top: 150px; font-size: 10.5px; line-height: 1.5; }
  .company__name { color: var(--brand-blue); font-weight: 700; margin-bottom: 3px; }
  .contact {
    position: absolute; left: 250px; top: 215px;
    display: grid; grid-template-columns: 74px auto; column-gap: 14px;
    font-size: 10px; line-height: 1.45;
  }
  .contact__label { font-weight: 700; }
  .contact__label--gap, .contact__value--gap { margin-top: 8px; }
  .logo-name {
    color: var(--brand-blue); font-weight: 700; text-align: center; line-height: 1;
  }
  .logo-name__initials { font-size: 92px; letter-spacing: 4px; }
  .logo-name__word { font-size: 20px; letter-spacing: 9px; margin-top: 10px; }
</style>
</head>
<body>
<main class="stage">
  <section class="card card--details" aria-label="Business card, details side">
    <div class="accent-bar"></div>
    <div class="person">
      <h1 class="person__name">Marla Denholm</h1>
      <p class="person__title">Chief Executive Officer</p>
      <div class="person__dash"></div>
    </div>
    <address class="company" style="font-style: normal;">
      <p class="company__name">fieldmark, Co. Ltd</p>
      <p>48 Ridge Lane, 3rd Building</p>
      <p>Cedar Falls City</p>
      <p>CF - 40718</p>
    </address>
    <div class="contact">
      <span class="contact__label">Telp.</span>
      <span>+00 (482) 6310 000<br>+00 (305) 7724 118</span>
      <span class="contact__label contact__label--gap">E-Mail</span>
      <span class="contact__value--gap">marla@fieldmark.com</span>
      <span class="contact__label">Website</span>
      <span>www.fieldmark.com</span>
    </div>
  </section>

  <section class="card card--logo" aria-label="Business card, logo side">
    <div class="logo-name">
      <div class="logo-name__initials">RW</div>
      <div class="logo-name__word">FRAMEWORKS</div>
    </div>
  </section>
</main>
</body>
</html>
```